Business Card for Orvane Parts Wholesale supplier

Hi There! I need a new business card for our company. We are specialized in selling Orvane parts, mostly we sell new LCD screens for Telvox and Slatrons. I would like to see that back in the design.

You can find the colors and logo's on our website: www.dorvak-example.nl

Industry/Entity Type

Business

Contact Information for Business Card

My Details:
Lars Vintorp

Phone: 0031612873406
E-mail: Lars@dorvak-example.nl

Slogan: "Because Quality Matters"

Font styles to use
Sans Serif

Colors

Designer to choose colors to be used in the design.

Requirements
Must have
• A Black backside with the Dorvak logo on it. The front side should be clean with only my contact details.
• But I'm also open for something really different or awesome!
Nice to have
• Remember that we are in the parts & repairing industry, So i'll be handing those business cards mainly to repair companies. Maybe you can do something with that thought :)

```html
<!DOCTYPE html>
<html lang="en">
<head>
<meta charset="utf-8">
<title>Dorvak Business Card</title>
<link href="https://fonts.googleapis.com/css2?family=Oswald:wght@500&family=Exo+2:wght@400;600&display=swap" rel="stylesheet">
<style>
  :root {
    --backdrop: #2b2b2b;
    --card: #a0a0a0;
    --card-mark: #8b8b8b;
    --ink: #ffffff;
    --ink-soft: #f2f2f2;
  }
  html, body {
    margin: 0;
    padding: 0;
    width: 1200px;
    height: 1000px;
    overflow: hidden;
    background: var(--backdrop);
  }
  .stage {
    position: relative;
    width: 1200px;
    height: 1000px;
  }
  .card {
    position: absolute;
    top: 345px;
    width: 540px;
    height: 310px;
    background: var(--card);
    overflow: hidden;
    box-shadow: 0 10px 30px rgba(0,0,0,0.45);
  }
  .card--contact { left: 45px; }
  .card--brand { left: 615px; }
  .card__mark {
    position: absolute;
    right: 55px;
    top: 30px;
    width: 230px;
    height: 230px;
    border-radius: 50%;
    background: var(--card-mark);
  }
  .contact {
    position: absolute;
    left: 34px;
    bottom: 34px;
    color: var(--ink);
  }
  .contact__name {
    font-family: "Oswald", sans-serif;
    font-weight: 500;
    font-size: 26px;
    letter-spacing: 0.5px;
    text-transform: uppercase;
    margin: 0 0 10px;
    line-height: 1;
  }
  .contact__list {
    list-style: none;
    margin: 0;
    padding: 0;
    font-family: "Exo 2", sans-serif;
    font-size: 15px;
    color: var(--ink-soft);
  }
  .contact__item {
    display: flex;
    align-items: center;
    gap: 12px;
    margin-top: 6px;
  }
  .contact__icon {
    width: 14px;
    height: 14px;
    fill: var(--ink);
    flex: none;
  }
  .brand {
    position: absolute;
    left: 34px;
    bottom: 40px;
    color: var(--ink);
    font-family: "Exo 2", sans-serif;
  }
  .brand__name {
    display: flex;
    align-items: center;
    gap: 10px;
    font-weight: 600;
    font-size: 36px;
    line-height: 1;
    text-transform: lowercase;
  }
  .brand__dot {
    width: 28px;
    height: 28px;
    border-radius: 50%;
    background: var(--ink);
  }
  .brand__slogan {
    margin: 6px 0 0 4px;
    font-weight: 400;
    font-size: 15px;
    letter-spacing: 0.4px;
  }
</style>
</head>
<body>
<main class="stage">
  <section class="card card--contact" aria-label="Card front with contact details">
    <div class="card__mark" aria-hidden="true"></div>
    <div class="contact">
      <h1 class="contact__name">Lars Vintorp</h1>
      <ul class="contact__list">
        <li class="contact__item">
          <svg class="contact__icon" viewBox="0 0 16 16" aria-hidden="true"><path d="M3.6 1.2l2.3 2.8-1.4 1.8c.9 2 2.5 3.6 4.5 4.5l1.8-1.4 2.8 2.3-1.5 2.6C7.6 13.4 2.6 8.4 1 3.1z"/></svg>
          <span>0031612873406</span>
        </li>
        <li class="contact__item">
          <svg class="contact__icon" viewBox="0 0 16 16" aria-hidden="true"><path d="M1 3h14v10H1z M2 4l6 5 6-5" fill="none" stroke="#fff" stroke-width="1.4"/></svg>
          <span>Lars@dorvak-example.nl</span>
        </li>
        <li class="contact__item">
          <svg class="contact__icon" viewBox="0 0 16 16" aria-hidden="true"><circle cx="8" cy="8" r="6.5" fill="none" stroke="#fff" stroke-width="1.3"/><ellipse cx="8" cy="8" rx="2.8" ry="6.5" fill="none" stroke="#fff" stroke-width="1.1"/><path d="M1.5 8h13" stroke="#fff" stroke-width="1.1"/></svg>
          <span>www.dorvak-example.nl</span>
        </li>
      </ul>
    </div>
  </section>

  <section class="card card--brand" aria-label="Card back with company name">
    <div class="card__mark" aria-hidden="true"></div>
    <div class="brand">
      <div class="brand__name"><span class="brand__dot" aria-hidden="true"></span><span>dorvak</span></div>
      <p class="brand__slogan">Because Quality Matters</p>
    </div>
  </section>
</main>
</body>
</html>
```